Awards Banquet Invitation

The Millbrook Valley Chamber of Commerce is celebrating it's 65th year at our Annual Awards Banquet (business leader awards). Since we were founded in 1950, we will have a 1950's theme. Dress will be 1950's Formal. I don't want cheesy 1950's. I want Classic feel and fonts from that era. This event is for business professionals so looks from ads in the 50's would be good for inspiration. I would like a look that I can use for the program and event ads. Invitation will include an RSVP insert. Date: February 10, 2015. Time: 6 cocktails, 7 dinner & program, Location: Delwen Oaks Country Club. Dress is 1950's formal

Target Market(s)

Business owners - our members

Industry/Entity Type

Business

• Lasalle, linotype, thirsty

Colors
86cfc6
474747
ffffff
000000

Requirements
Must have
• classic 50's font and old-fashioned feel
Should not have
• sock hop, soda fountain, 50's diner

```html
<!DOCTYPE html>
<html lang="en">
<head>
<meta charset="utf-8">
<title>Annual Awards Banquet Invitation</title>
<link rel="stylesheet" href="https://fonts.googleapis.com/css2?family=Lobster&family=Poiret+One&family=Old+Standard+TT:wght@700&display=swap">
<style>
  :root {
    --ink: #3b2f16;
    --band-dark: #4b4023;
    --band-light: #8c866a;
    --gold-edge: #dcc172;
    --gold-mid: #e3d08f;
    --gold-center: #e4e0b0;
  }
  html, body {
    margin: 0;
    padding: 0;
    overflow: hidden;
    background: #ffffff;
  }
  .invitation {
    position: relative;
    width: 900px;
    height: 1200px;
    overflow: hidden;
    background: radial-gradient(ellipse 60% 55% at 50% 55%, var(--gold-center) 0%, var(--gold-mid) 55%, var(--gold-edge) 100%);
    color: var(--ink);
    text-align: center;
  }
  .damask-band {
    position: absolute;
    left: 0;
    width: 900px;
    background: linear-gradient(180deg, var(--band-dark), #5e5636 50%, var(--band-dark));
  }
  .damask-band--top { top: 0; height: 152px; }
  .damask-band--bottom { top: 1010px; height: 190px; }
  .line {
    position: absolute;
    left: 0;
    width: 900px;
    margin: 0;
    line-height: 1;
  }
  .host {
    top: 176px;
    font-family: "Lobster", cursive;
    font-size: 40px;
  }
  .deco {
    font-family: "Poiret One", sans-serif;
  }
  .celebrating { top: 268px; font-size: 30px; }
  .anniversary { top: 318px; font-size: 86px; }
  .at-our { top: 416px; font-size: 22px; }
  .event-title {
    top: 478px;
    font-family: "Lobster", cursive;
    font-size: 82px;
    line-height: 86px;
    font-weight: 400;
  }
  .subtitle {
    top: 668px;
    font-family: "Old Standard TT", serif;
    font-weight: 700;
    font-size: 26px;
  }
  .detail { font-size: 23px; line-height: 30px; }
  .date { top: 726px; }
  .time { top: 795px; }
  .location { top: 892px; }
  .dress-code { top: 948px; font-size: 31px; }
</style>
</head>
<body>
  <main class="invitation">
    <div class="damask-band damask-band--top" role="img" aria-label="Dark olive damask floral pattern band"></div>

    <p class="line host">The Millbrook Valley Chamber of Commerce</p>
    <p class="line deco celebrating">is celebrating it's</p>
    <p class="line deco anniversary">65th year</p>
    <p class="line deco at-our">at our</p>
    <h1 class="line event-title">Annual Awards<br>Banquet</h1>
    <p class="line subtitle">(Business Leader Awards)</p>
    <p class="line deco detail date">Date: February 10, 2015.</p>
    <p class="line deco detail time">Time: 6 o'clock Cocktails,<br>7 o'clock Dinner &amp; Program</p>
    <p class="line deco detail location">Location: Delwen Oaks Country Club</p>
    <p class="line deco dress-code">Dress Code is 1950's Formal</p>

    <div class="damask-band damask-band--bottom" role="img" aria-label="Dark olive damask floral pattern band"></div>
  </main>
</body>
</html>
```